Business Card Design Project

The business card is for an educational company that provides personalised tuition to students.

The company logo is in orange and blue (as provided) and should be included in the name card design

The philosophy of the company is to make learning a comfortable experience for student as such design of the namecard should look fresh and has a bit of the 'wow' factor. Some of the namecard design that appeals to me are as uploaded under Sample Design.

The particulars that need to be provided are:
(1): Company Name (Quillmont Education)
(1): Name
(2): Educational qualifications which will appear below name
(3): Mobile number
(4): Email address
(5): Website

Industry/Entity Type

Business

Requirements
Must have
• (1): Company Logo

(2): The card background should preferably be coloured both for the front side and back.

(3): The choice of font is important as part of the selection consideration. There is no preferred font that I have selected, designer is free to choose the font that will complement their design.

```html
<!DOCTYPE html>
<html lang="en">
<head>
<meta charset="utf-8">
<title>Quillmont Education – Business Card</title>
<link rel="stylesheet" href="https://fonts.googleapis.com/css2?family=Caladea&family=Fira+Sans:wght@600&display=swap">
<style>
  :root {
    --page-bg: #f4f4f2;
    --green-light: #a6d64a;
    --green-mid: #8cc63f;
    --green-deep: #6fa82a;
    --stripe-red: #b0101a;
    --band-red: #a00d14;
    --panel-gold: rgba(236, 196, 64, 0.55);
    --panel-gold-soft: rgba(236, 212, 90, 0.25);
    --brand-slate: #3f5670;
    --ink: #111111;
    --white: #ffffff;
    --pattern-lime: #a3cf2a;
    --pattern-black: #1b1b1b;
    --pattern-white: #f2f2f2;
  }
  html, body {
    margin: 0;
    padding: 0;
    width: 1200px;
    height: 835px;
    overflow: hidden;
    background: var(--page-bg);
  }
  .canvas {
    position: relative;
    width: 1200px;
    height: 835px;
  }
  .card {
    position: absolute;
    width: 700px;
    height: 340px;
    overflow: hidden;
  }
  .card--front {
    left: 60px;
    top: 45px;
    background: linear-gradient(160deg, var(--green-light) 0%, var(--green-mid) 45%, var(--green-deep) 100%);
  }
  .card--back {
    left: 440px;
    top: 450px;
    background: linear-gradient(135deg, var(--pattern-lime) 0%, #7e9a3a 40%, var(--pattern-black) 55%, #8a8a8a 75%, var(--pattern-white) 100%);
  }
  .brand {
    position: absolute;
    left: 22px;
    top: 128px;
    display: flex;
    align-items: center;
    gap: 12px;
  }
  .brand__square {
    width: 54px;
    height: 54px;
    background: var(--brand-slate);
  }
  .brand__name {
    font-family: "Fira Sans", sans-serif;
    font-weight: 600;
    font-size: 29px;
    line-height: 1.05;
    color: var(--brand-slate);
    margin: 0;
  }
  .stripe {
    position: absolute;
    top: 0;
    bottom: 0;
    background: var(--stripe-red);
  }
  .stripe--first { left: 248px; width: 8px; }
  .stripe--second { left: 266px; width: 9px; }
  .panel {
    position: absolute;
    left: 300px;
    top: 20px;
    width: 330px;
    height: 258px;
    border-radius: 32px;
    background: linear-gradient(200deg, var(--panel-gold-soft) 0%, var(--panel-gold) 100%);
  }
  .person {
    position: absolute;
    left: 280px;
    right: 0;
    top: 58px;
    text-align: center;
    font-family: "Caladea", serif;
    color: var(--ink);
  }
  .person__name {
    margin: 0;
    font-size: 33px;
    font-weight: 400;
    line-height: 1.1;
  }
  .person__degree {
    margin: 2px 0 0;
    font-size: 17px;
  }
  .contact {
    position: absolute;
    left: 292px;
    top: 248px;
    margin: 0;
    font-family: "Caladea", serif;
    font-size: 16px;
    line-height: 26px;
    color: var(--ink);
  }
  .contact__label {
    display: inline-block;
    width: 64px;
  }
  .web-band {
    position: absolute;
    left: 266px;
    right: 0;
    bottom: 0;
    height: 38px;
    background: var(--band-red);
    display: flex;
    align-items: center;
    justify-content: center;
    font-family: "Caladea", serif;
    font-size: 17px;
    color: var(--white);
  }
</style>
</head>
<body>
<main class="canvas">
  <section class="card card--front" aria-label="Business card front">
    <div class="brand">
      <span class="brand__square" aria-hidden="true"></span>
      <p class="brand__name">Quillmont<br>Education</p>
    </div>
    <span class="stripe stripe--first" aria-hidden="true"></span>
    <span class="stripe stripe--second" aria-hidden="true"></span>
    <span class="panel" aria-hidden="true"></span>
    <div class="person">
      <h1 class="person__name">Farhan Idris Malik</h1>
      <p class="person__degree">Computer science (BS)</p>
    </div>
    <p class="contact">
      <span class="contact__label">Mobile :</span>+9215550187<br>
      <span class="contact__label">Email &nbsp;:</span>farhanmalik@email.com
    </p>
    <div class="web-band">www.farhanmalik.com</div>
  </section>
  <section class="card card--back" role="img" aria-label="Card back: harlequin diamond pattern in lime green, black and white"></section>
</main>
</body>
</html>
```